Garage Door Company seeking business card designs.
Harbor Ridge Door
Professional
Miles Tandry
Owner, Operator.
We don't want a address listed...
Miles@HarborRidgeDoor.com
www.PortalLiftExperts.com
We want to publish three numbers: Winsted - 320.555.0147 Glencoe - 320.555.0192 St. Boni - 952.555.0163 on front... Commercial and Residential On back... New Garage Door Sales and Installation. Repair and Maintenance Services. List website; www.PortalLiftExperts.com Have name, title, phone numbers, email, and website on one side. Motto's and verbiage on the other back side. Logo likely on front very prominently. Front can be full color, and back should be back letter, or the door of the logo lettering.
"If you can't get it up, we can!" Sales and Installation. Repair and Maintenance.

```html
<!DOCTYPE html>
<html lang="en">
<head>
<meta charset="utf-8">
<title>Harbor Ridge Door – Business Cards</title>
<link rel="stylesheet" href="https://fonts.googleapis.com/css2?family=Open+Sans:ital,wght@0,400;0,600;0,700;1,400&display=swap">
<style>
  :root{
    --forest:#3f4f1c;
    --forest-deep:#2f3c12;
    --paper:#ffffff;
    --ink:#3a3a3a;
    --muted:#6b6b6b;
    --stage:#e9eae6;
    --cream:#f3f4ea;
  }
  *{box-sizing:border-box;margin:0;padding:0}
  html,body{width:1200px;height:904px;overflow:hidden}
  body{
    background:var(--stage);
    font-family:"Open Sans",Arial,sans-serif;
    display:flex;flex-direction:column;align-items:center;justify-content:center;gap:40px;
  }
  .card{
    width:700px;height:400px;border-radius:22px;position:relative;overflow:hidden;
    box-shadow:0 6px 18px rgba(0,0,0,.18);
  }
  /* back side */
  .card-back{background:var(--forest);color:var(--cream);text-align:center;
    display:flex;flex-direction:column;align-items:center;padding-top:34px}
  .logo-art{border-radius:6px}
  .card-back .logo-art{width:150px;height:96px;
    background:linear-gradient(180deg,#7e8a5c,#5a6a30)}
  .brand-name{font-weight:700;font-size:34px;letter-spacing:.5px;line-height:1.1;margin-top:10px}
  .card-back .brand-name{color:var(--cream)}
  .motto{font-style:italic;font-size:17px;margin-top:16px}
  .services{font-size:16px;line-height:1.45;margin-top:18px}
  .site-line{display:flex;align-items:center;gap:12px;margin-top:22px;font-size:16px}
  .site-line::before,.site-line::after{content:"";width:40px;height:1px;background:var(--cream)}
  /* front side */
  .card-front{background:var(--paper);color:var(--ink)}
  .name-block{position:absolute;left:0;top:118px;padding-left:50px}
  .name-block::before{content:"";position:absolute;left:0;top:4px;width:26px;height:44px;background:var(--forest)}
  .person-name{font-weight:700;font-size:24px;color:var(--forest)}
  .person-title{font-size:16px;color:var(--muted);margin-top:2px}
  .contact-list{position:absolute;left:50px;bottom:38px;list-style:none;font-size:15.5px;line-height:1.5;color:var(--ink)}
  .contact-list li{display:flex;align-items:center;gap:12px}
  .contact-list svg{width:16px;height:16px;flex:none}
  .front-brand{position:absolute;right:50px;top:60px;text-align:center;width:250px;
    display:flex;flex-direction:column;align-items:center}
  .card-front .logo-art{width:190px;height:110px;background:linear-gradient(180deg,#5d6e34,#2f3c12)}
  .card-front .brand-name{color:var(--forest);font-size:28px}
  .tagline{font-size:17px;color:var(--forest);margin-top:6px}
  .front-edge{position:absolute;left:0;right:0;bottom:0;height:10px;background:var(--forest)}
</style>
</head>
<body>

<section class="card card-back">
  <div class="logo-art" role="img" aria-label="Logo illustration: pine trees behind a garage with a door"></div>
  <div class="brand-name">Harbor Ridge Door</div>
  <p class="motto">“If you can’t get it up, we can!”</p>
  <p class="services">Sales and Installation,<br>Repair and Maintenance</p>
  <p class="site-line">www.PortalLiftExperts.com</p>
</section>

<section class="card card-front">
  <div class="name-block">
    <div class="person-name">Miles Tandry</div>
    <div class="person-title">Owner, Operator</div>
  </div>

  <ul class="contact-list">
    <li><svg viewBox="0 0 16 16"><circle cx="8" cy="8" r="8" fill="#3f4f1c"/><path d="M5.5 4.5l1.5 0 .8 2-1 .8a5 5 0 0 0 2 2l.8-1 2 .8v1.5c0 .5-.5 1-1 1A7 7 0 0 1 4.5 5.5c0-.5.5-1 1-1z" fill="#fff"/></svg>320.555.0147 (Winsted)</li>
    <li><svg viewBox="0 0 16 16"><circle cx="8" cy="8" r="8" fill="#3f4f1c"/><path d="M5.5 4.5l1.5 0 .8 2-1 .8a5 5 0 0 0 2 2l.8-1 2 .8v1.5c0 .5-.5 1-1 1A7 7 0 0 1 4.5 5.5c0-.5.5-1 1-1z" fill="#fff"/></svg>320.555.0192 (Glencoe)</li>
    <li><svg viewBox="0 0 16 16"><circle cx="8" cy="8" r="8" fill="#3f4f1c"/><path d="M5.5 4.5l1.5 0 .8 2-1 .8a5 5 0 0 0 2 2l.8-1 2 .8v1.5c0 .5-.5 1-1 1A7 7 0 0 1 4.5 5.5c0-.5.5-1 1-1z" fill="#fff"/></svg>952.555.0163 (St. Boni)</li>
    <li><svg viewBox="0 0 16 16"><circle cx="8" cy="8" r="8" fill="#3f4f1c"/><rect x="4" y="5" width="8" height="6" fill="none" stroke="#fff" stroke-width="1.2"/><path d="M4 5l4 3.5L12 5" fill="none" stroke="#fff" stroke-width="1.2"/></svg>Miles@HarborRidgeDoor.com</li>
    <li><svg viewBox="0 0 16 16"><circle cx="8" cy="8" r="8" fill="#3f4f1c"/><circle cx="8" cy="8" r="4" fill="none" stroke="#fff" stroke-width="1.2"/><path d="M4 8h8M8 4c-2 2.5-2 5.5 0 8M8 4c2 2.5 2 5.5 0 8" fill="none" stroke="#fff" stroke-width="1"/></svg>www.PortalLiftExperts.com</li>
  </ul>

  <div class="front-brand">
    <div class="logo-art" role="img" aria-label="Logo illustration: pine trees behind a garage with a door"></div>
    <div class="brand-name">Harbor Ridge Door</div>
    <div class="tagline">Commercial and Residential</div>
  </div>

  <div class="front-edge"></div>
</section>

</body>
</html>
```